business card design for a small scale specialty cut flower farm

We need a business card design for Hollowmere Blossom Farm based in Langley, BC, Canada. We produce specialty, high-end cut flowers and sell locally to florists, local shops and markets and the end user through bouquet subscriptions. The final business card design should be memorable and have a timeless or vintage feel. We would prefer a square shape.

Target Market(s)

florists, shops and seasonal markets, local flower lovers

Industry/Entity Type

Floral

Contact Information for Business Card

Maren Tilde Hofstad, Grower
Langley, BC, Canada
website: hollowmereblossomfarm.com
instagram: @hollowmereblossomfarm
Tel: 604.913.2748
facebook: www.facebook.com/hollowmereblooms/

Font styles to use
Serif
Decorative
Script

Requirements
Must have
• soft black background colour on front side, the included logo and catch phrase: Fresh Local Seasonal
Nice to have
• phone number and website address on front of card, included photo 6539 incorporated onto the back, possibly photo 6609 as well.

```html
<!DOCTYPE html>
<html lang="en">
<head>
<meta charset="utf-8">
<title>Hollowmere Blossom Farm – Business Cards</title>
<link href="https://fonts.googleapis.com/css2?family=Great+Vibes&family=Lato:wght@400;700&family=Open+Sans:wght@400;600&display=swap" rel="stylesheet">
<style>
  :root {
    --page-bg: #e9e7e4;
    --soft-black: #2b2b2c;
    --card-white: #ffffff;
    --ink: #1e1e1e;
    --text-light: #f4f4f4;
    --sage: #6f9a62;
    --sage-soft: #8db07f;
    --petal-pink: #e58bb8;
    --muted: #555555;
  }
  * { box-sizing: border-box; margin: 0; padding: 0; }
  html, body {
    width: 1200px; height: 900px; overflow: hidden;
    background: var(--page-bg);
  }
  .sheet {
    position: relative; width: 1200px; height: 900px;
    display: flex; flex-direction: column; align-items: center;
    justify-content: center; gap: 36px;
  }
  .card {
    position: relative; width: 700px; height: 400px;
    overflow: hidden; border-radius: 4px;
    box-shadow: 0 6px 20px rgba(0,0,0,.18);
  }

  /* Front */
  .card--front { background: var(--soft-black); color: var(--text-light); }
  .front-brand {
    position: absolute; left: 0; right: 0; top: 70px;
    display: flex; flex-direction: column; align-items: center;
  }
  .brand-dot {
    width: 56px; height: 56px; border-radius: 50%;
    background: var(--petal-pink); margin-bottom: 26px;
  }
  .brand-name {
    font-family: 'Lato', sans-serif; font-weight: 400;
    font-size: 34px; letter-spacing: 7px; text-transform: uppercase;
    text-align: center;
  }
  .brand-tagline {
    font-family: 'Lato', sans-serif; font-size: 12px;
    letter-spacing: 5px; text-transform: uppercase;
    margin-top: 18px; opacity: .85;
  }
  .front-footer {
    position: absolute; left: 50px; right: 50px; bottom: 36px;
    display: flex; justify-content: space-between; align-items: baseline;
    font-family: 'Open Sans', sans-serif; font-size: 17px;
  }
  .catchphrase {
    color: var(--sage-soft); text-transform: uppercase; font-size: 17px;
    letter-spacing: .5px;
  }

  /* Back */
  .card--back { background: var(--card-white); color: var(--ink); }
  .back-info { position: absolute; left: 40px; top: 40px; width: 390px; }
  .back-brand .brand-name { color: var(--ink); font-size: 26px; letter-spacing: 5px; text-align: left; }
  .back-brand .brand-tagline { color: var(--muted); font-size: 10px; margin-top: 10px; letter-spacing: 4px; }
  .person { position: relative; margin-top: 34px; padding-left: 16px; }
  .person::before {
    content: ""; position: absolute; left: 0; top: 6px;
    width: 6px; height: 58px; background: var(--petal-pink);
  }
  .person-name {
    font-family: 'Great Vibes', cursive; font-size: 40px;
    color: var(--sage); line-height: 1; white-space: nowrap;
  }
  .person-role {
    font-family: 'Open Sans', sans-serif; font-size: 17px; margin-top: 4px;
  }
  .contact-list {
    list-style: none; margin-top: 26px;
    font-family: 'Open Sans', sans-serif; font-size: 17px;
  }
  .contact-list li {
    display: flex; align-items: center; gap: 10px; line-height: 27px;
    white-space: nowrap;
  }
  .contact-icon { width: 16px; height: 16px; flex: none; }
  .photo-frame {
    position: absolute; left: 420px; top: 20px;
    width: 420px; height: 420px; border-radius: 50%;
    border: 3px solid var(--sage);
    background:
      radial-gradient(circle at 45% 30%, #e2506a 0%, #a0224a 28%, transparent 55%),
      radial-gradient(circle at 60% 10%, #7a5bb8 0%, transparent 35%),
      linear-gradient(180deg, #c74066 0%, #8f3050 38%, #b8c7d8 60%, #dde5ee 100%);
  }
</style>
</head>
<body>
<main class="sheet">

  <section class="card card--front" aria-label="Card front">
    <div class="front-brand">
      <span class="brand-dot" aria-hidden="true"></span>
      <h1 class="brand-name">Hollowmere Blossom Farm</h1>
      <p class="brand-tagline">Specialty Cut Flowers · Est. 2019</p>
    </div>
    <div class="front-footer">
      <span class="front-phone">(604) 913-2748</span>
      <span class="catchphrase">Fresh Local Seasonal</span>
      <span class="front-web">hollowmereblossomfarm.com</span>
    </div>
  </section>

  <section class="card card--back" aria-label="Card back">
    <div class="back-info">
      <div class="back-brand">
        <h2 class="brand-name">Hollowmere Blossom Farm</h2>
        <p class="brand-tagline">Specialty Cut Flowers · Est. 2019</p>
      </div>
      <div class="person">
        <p class="person-name">Maren Tilde Hofstad</p>
        <p class="person-role">Owner</p>
      </div>
      <ul class="contact-list">
        <li>
          <svg class="contact-icon" viewBox="0 0 16 16" aria-hidden="true"><path d="M4 1.5l2.2 2.6-1.2 1.6c.8 1.9 2.4 3.5 4.3 4.3l1.6-1.2 2.6 2.2-1.3 2.3C7 13 3 9 1.7 2.8z" fill="none" stroke="var(--sage)" stroke-width="1.4" stroke-linejoin="round"/></svg>
          (604) 913-2748
        </li>
        <li>
          <svg class="contact-icon" viewBox="0 0 16 16" aria-hidden="true"><rect x="1.5" y="1.5" width="13" height="13" rx="3" fill="none" stroke="var(--sage)" stroke-width="1.6"/></svg>
          @hollowmereblossomfarm
        </li>
        <li>
          <svg class="contact-icon" viewBox="0 0 16 16" aria-hidden="true"><rect x="1" y="1" width="14" height="14" rx="2" fill="var(--sage)"/></svg>
          petalcircle.net/hollowmereblooms/
        </li>
        <li>
          <svg class="contact-icon" viewBox="0 0 16 16" aria-hidden="true"><g fill="none" stroke="var(--sage)" stroke-width="1.3"><circle cx="8" cy="8" r="6.5"/><ellipse cx="8" cy="8" rx="3" ry="6.5"/><path d="M1.5 8h13"/></g></svg>
          www.hollowmereblossomfarm.com
        </li>
      </ul>
    </div>
    <div class="photo-frame" role="img" aria-label="Photo of deep red and pink dahlias in a galvanised metal bucket"></div>
  </section>

</main>
</body>
</html>
```